Gardener needs an exciting new flyer design.

I'm a passionate gardener that requires a custom flyer design for a owner operator gardening business. Design will be for a DL flyer. I'm based on the Sunshine coast in Queensland Australia. My target audience is the residential market on the Sunshine coast. Business name is Marlowe Greens. My services are, lawn mowing, weeding, Eco Friendly fertilizing, green waste removal, Mulching, tree and shrub pruning, Full garden makeovers, hedging, pressure cleaning, privacy screening, Timber deck rejuvenation, Planting, Turf preparation and installation, and much more. Free no obligation quotes, reliable and friendly service, great rates. 12 years experience. Web www.marlowegreens.com.au - Phone 0418527064 - Email doug@marlowegreens.com.au I would like the design to portray a friendly and professional approach.

Target Market(s)

Residential

Industry/Entity Type

Gardener

Font styles to use
Serif

Colors
9ccb3b
abd037
3176b5

Requirements
Must have
• my services, my logo, my contact details,

```html
<!DOCTYPE html>
<html lang="en">
<head>
<meta charset="utf-8">
<title>Marlowe Greens – DL Flyer</title>
<link rel="stylesheet" href="https://fonts.googleapis.com/css2?family=Open+Sans:wght@400;600;700&display=swap">
<style>
  :root {
    --lime: #8cc63e;
    --lime-light: #a8d44c;
    --lime-deep: #76b52f;
    --panel: rgba(150, 201, 62, 0.9);
    --paper: #ffffff;
    --mist: #eeeeee;
    --backdrop: #e6e0d7;
    --ink-white: #ffffff;
    --frame: #8cc63e;
  }
  * { box-sizing: border-box; margin: 0; padding: 0; }
  html, body { width: 1200px; height: 900px; overflow: hidden; }
  body {
    background: var(--backdrop);
    font-family: "Open Sans", Arial, sans-serif;
    display: flex; align-items: center; justify-content: center;
  }
  .flyer {
    position: relative;
    width: 400px; height: 848px;
    background: var(--paper);
    overflow: hidden;
    box-shadow: 0 6px 24px rgba(0,0,0,0.18);
  }
  /* hero */
  .hero { position: relative; height: 372px; }
  .hero-photo {
    position: absolute; inset: 0;
    background: linear-gradient(180deg, #6fb2e6 0%, #a9d3ef 28%, #9cc27a 46%, #5e9a3a 62%, #62b337 100%);
  }
  .brand-badge {
    position: absolute; top: 12px; right: 14px;
    width: 128px; height: 76px; border-radius: 50%;
    background: var(--paper); border: 4px solid var(--lime-light);
    display: flex; align-items: center; justify-content: center;
  }
  .brand-badge span { font-size: 14px; font-weight: 600; color: var(--lime-deep); }
  .intro {
    position: absolute; top: 44px; left: 14px;
    width: 216px; height: 318px;
    background: var(--panel);
    color: var(--ink-white);
    padding: 12px 12px;
  }
  .intro h1 { font-size: 18px; font-weight: 600; margin-bottom: 4px; line-height: 1.2; }
  .intro p { font-size: 12.2px; line-height: 1.32; }
  /* band */
  .tagline {
    height: 70px;
    background: linear-gradient(90deg, var(--lime-light), var(--lime));
    color: var(--ink-white);
    display: flex; align-items: center; justify-content: center; text-align: center;
    font-size: 15.5px; font-weight: 600; line-height: 1.3;
    padding: 0 12px;
  }
  /* services */
  .services {
    height: 250px;
    background: linear-gradient(90deg, var(--paper), var(--mist));
    display: flex; align-items: center; gap: 12px;
    padding: 0 10px 0 12px;
  }
  .garden-frame {
    flex: 0 0 176px; height: 214px;
    border: 2px solid var(--frame); padding: 6px; background: var(--paper);
  }
  .garden-photo {
    width: 100%; height: 100%;
    background: linear-gradient(180deg, #2f6a2a 0%, #4e8a3a 40%, #8a6fc0 62%, #b49bd6 80%, #d8d2c2 100%);
  }
  .service-list { list-style: none; color: var(--lime-deep); font-size: 12.4px; line-height: 1.45; }
  .service-list li { display: flex; align-items: flex-start; gap: 6px; }
  .service-list svg { flex: 0 0 11px; width: 11px; height: 11px; margin-top: 4px; }
  /* contact */
  .contact {
    height: 156px;
    background: linear-gradient(90deg, var(--lime-light), var(--lime));
    color: var(--ink-white);
    display: flex; flex-direction: column; align-items: center; justify-content: center;
    text-align: center;
  }
  .contact h2 { font-size: 26px; font-weight: 700; letter-spacing: 0.5px; margin-bottom: 4px; }
  .contact p { font-size: 17px; line-height: 1.3; }
</style>
</head>
<body>
<svg width="0" height="0" style="position:absolute">
  <symbol id="tick-box" viewBox="0 0 12 12">
    <rect x="0.75" y="1.75" width="9.5" height="9.5" fill="none" stroke="#76b52f" stroke-width="1.5"/>
    <path d="M2.5 6.2 L5 8.7 L11.2 1.2" fill="none" stroke="#76b52f" stroke-width="2" stroke-linecap="round" stroke-linejoin="round"/>
  </symbol>
</svg>

<main class="flyer">
  <section class="hero">
    <div class="hero-photo" role="img" aria-label="Photo of a cottage with clipped hedges and a wide green lawn under blue sky"></div>
    <div class="brand-badge"><span>Marlowe Greens</span></div>
    <div class="intro">
      <h1>Marlowe Greens</h1>
      <p>Marlowe Greens is your garden and lawn care specialist, with a passion for gardening and a keen eye for detail you can rest assured you're in the right hands.</p>
      <p>My services are tailored to meet every individual clients needs. From a one time mow too regular lawn mowing, all aspects of garden care and even full garden makeovers. I go that extra mile every time to leave you garden and yard looking amazing.</p>
    </div>
  </section>

  <div class="tagline">Marlowe Greens Provides Professsional<br>Lawn Care and Gardening Services</div>

  <section class="services">
    <div class="garden-frame">
      <div class="garden-photo" role="img" aria-label="Photo of a garden path lined with purple flowering plants and trees"></div>
    </div>
    <ul class="service-list">
      <li><svg><use href="#tick-box"/></svg>Lawn mowing</li>
      <li><svg><use href="#tick-box"/></svg>Weeding</li>
      <li><svg><use href="#tick-box"/></svg>Eco Friendly fertilizing</li>
      <li><svg><use href="#tick-box"/></svg>Green waste removal</li>
      <li><svg><use href="#tick-box"/></svg>Mulching</li>
      <li><svg><use href="#tick-box"/></svg>Tree and shrub pruning</li>
      <li><svg><use href="#tick-box"/></svg>Full garden makeovers</li>
      <li><svg><use href="#tick-box"/></svg>Hedging</li>
      <li><svg><use href="#tick-box"/></svg>Pressure cleaning</li>
      <li><svg><use href="#tick-box"/></svg>Privacy screening</li>
      <li><svg><use href="#tick-box"/></svg>Timber deck rejuvenation</li>
      <li><svg><use href="#tick-box"/></svg>Planting</li>
      <li><svg><use href="#tick-box"/></svg>Turf preparation and installation</li>
    </ul>
  </section>

  <section class="contact">
    <h2>Contact Us Now</h2>
    <p>0418527064</p>
    <p>www.marlowegreens.com.au</p>
    <p>doug@marlowegreens.com.au</p>
  </section>
</main>
</body>
</html>
```